Road Construction Company needs business cards

We would like a new business card designed for our business.

We're a road construction company based in Qld, Australia.

Can the business card please have the following information on it.

Name: Brent Halloway
Position: General Manager
Phone: 0491 257 314
Email: Brent.halloway@drovik.com.au
Address: 87 Margrove Ave, Tindale, QLD, 4016
Website: www.drovik.com.au

Visually we'd like the card to be professional and simple.

Attached is our logo.

Our website is www.drovik.com.au

Target Market(s)

Men aged 25-60

Contact Information for Business Card

As listed in project description

Font styles to use
Serif

Requirements
Must have
• Large logo on back of card

```html
<!DOCTYPE html>
<html lang="en">
<head>
<meta charset="utf-8">
<title>Drovik Business Cards</title>
<link rel="stylesheet" href="https://fonts.googleapis.com/css2?family=Alegreya+Sans:wght@400;800&family=Marcellus&display=swap">
<style>
  :root {
    --page: #e9ece9;
    --brand-blue: #0565b0;
    --ink-blue: #1a50a2;
    --white: #ffffff;
  }
  * { box-sizing: border-box; margin: 0; padding: 0; }
  html, body { width: 1200px; height: 1200px; overflow: hidden; }
  body {
    background: var(--page);
    font-family: "Alegreya Sans", sans-serif;
    position: relative;
  }
  .card {
    position: absolute;
    left: 200px;
    width: 800px;
    height: 489px;
    overflow: hidden;
    box-shadow: 0 6px 18px rgba(0,0,0,0.12);
  }
  .card-back { top: 80px; background: var(--brand-blue); }
  .card-front { top: 631px; background: var(--white); }

  /* back */
  .back-brand {
    position: absolute;
    top: 150px; left: 0; right: 0;
    display: flex; justify-content: center; align-items: center; gap: 22px;
    color: var(--white);
  }
  .brand-mark { width: 46px; height: 46px; background: currentColor; flex: none; }
  .brand-name {
    font-weight: 800;
    font-size: 104px;
    letter-spacing: 4px;
    line-height: 1;
    text-transform: uppercase;
    white-space: nowrap;
  }
  .back-web {
    position: absolute;
    top: 330px; left: 0; right: 0;
    text-align: center;
    color: var(--white);
    font-size: 30px;
    letter-spacing: 0.5px;
  }

  /* front */
  .front-panel { position: absolute; inset: 0; width: 100%; height: 100%; }
  .front-panel polygon { fill: var(--brand-blue); }
  .contact-list {
    position: absolute;
    left: 52px; top: 116px;
    list-style: none;
    color: var(--white);
    font-size: 22px;
    line-height: 1.15;
  }
  .contact-item { display: flex; align-items: flex-start; gap: 18px; margin-bottom: 24px; white-space: nowrap; }
  .contact-key {
    flex: 0 0 32px; height: 32px;
    background: var(--white);
    color: var(--brand-blue);
    border-radius: 6px;
    font-family: "Marcellus", serif;
    font-size: 19px;
    display: flex; align-items: center; justify-content: center;
    margin-top: -4px;
  }
  .identity {
    position: absolute;
    left: 478px; top: 110px;
    color: var(--ink-blue);
    white-space: nowrap;
  }
  .person-name { font-family: "Marcellus", serif; font-weight: 400; font-size: 36px; line-height: 1.05; }
  .person-role { font-family: "Marcellus", serif; font-size: 22px; margin-top: 4px; padding-left: 60px; }
  .front-brand {
    position: absolute;
    left: 505px; top: 275px;
    display: flex; align-items: center; gap: 12px;
    color: var(--ink-blue);
  }
  .front-brand .brand-mark { width: 24px; height: 24px; }
  .front-brand .brand-name { font-size: 52px; letter-spacing: 2px; }
</style>
</head>
<body>
  <section class="card card-back" aria-label="Card back">
    <div class="back-brand">
      <span class="brand-mark"></span>
      <span class="brand-name">Drovik</span>
    </div>
    <p class="back-web">www.drovik.com.au</p>
  </section>

  <section class="card card-front" aria-label="Card front">
    <svg class="front-panel" viewBox="0 0 800 489" preserveAspectRatio="none" aria-hidden="true">
      <polygon points="0,0 440,0 385,489 0,489"/>
    </svg>
    <ul class="contact-list">
      <li class="contact-item"><span class="contact-key">E</span><span>Brent.halloway@drovik.com.au</span></li>
      <li class="contact-item"><span class="contact-key">A</span><span>87 Margrove Ave, Tindale,<br>QLD, 4016</span></li>
      <li class="contact-item"><span class="contact-key">W</span><span>www.drovik.com.au</span></li>
      <li class="contact-item"><span class="contact-key">P</span><span>0491 257 314</span></li>
    </ul>
    <div class="identity">
      <h1 class="person-name">Brent Halloway</h1>
      <p class="person-role">General Manager</p>
    </div>
    <div class="front-brand">
      <span class="brand-mark"></span>
      <span class="brand-name">Drovik</span>
    </div>
  </section>
</body>
</html>
```